Design eines privaten Leadership-Leitbildes
Zielgruppe
Es geht um mein privates Leadership-Leitbild. Ich bin CEO eines Unternehmens, das sich in der Schweiz und international intensiv mit der Digitalen Transformation im Bauwesen befasst (www.tlv-bau.ch).
Aufgabenstellung
Die Vorlage ist bereits recht konkret und beinhaltet alles. In der grafischen Aufbereitung ist der Kreative frei. Allerdings geht es um einen Business-Content und bei meinem Leadership-Leitbild um meine persönliche 'Visitenkarte'. Also nicht 'verspielt' oder 'witzig'. Das Plakat soll A4 und A3 genutzt werden und auch auf einem gängigen Laser-Drucker in guter Qualität ausgedruckt werden können.

```html
<!DOCTYPE html>
<html lang="de">
<head>
<meta charset="utf-8">
<title>Leadership-Leitbild – tlv bau</title>
<link href="https://fonts.googleapis.com/css2?family=Bebas+Neue&family=Open+Sans:wght@400;600&display=swap" rel="stylesheet">
<style>
  :root {
    --bg: #4a4a4c;
    --bg-pattern: #414143;
    --orange: #d07a2d;
    --white: #ffffff;
  }
  * { margin: 0; padding: 0; box-sizing: border-box; }
  html, body { width: 848px; height: 1200px; overflow: hidden; background: var(--bg); }
  .poster {
    position: relative;
    width: 848px;
    height: 1200px;
    background: var(--bg);
    color: var(--white);
    font-family: "Open Sans", Arial, sans-serif;
    overflow: hidden;
  }
  .skyline {
    position: absolute;
    left: 0; top: 230px;
    width: 848px; height: 970px;
    background: linear-gradient(180deg, rgba(65,65,67,0) 0%, var(--bg-pattern) 35%, var(--bg-pattern) 80%, rgba(65,65,67,0.4) 100%);
  }
  .brand {
    position: absolute;
    left: 70px; top: 18px;
    display: flex;
    align-items: flex-end;
    gap: 16px;
  }
  .brand-name {
    font-weight: 600;
    font-size: 44px;
    line-height: 1;
    letter-spacing: 1px;
  }
  .brand-tagline {
    font-size: 13px;
    font-weight: 400;
    letter-spacing: 0.5px;
    padding-bottom: 4px;
  }
  .pillars {
    position: absolute;
    left: 71px; top: 145px;
    display: flex;
    gap: 26px;
  }
  .pillar {
    width: 156px; height: 156px;
    border-radius: 50%;
    background: var(--orange);
    display: flex;
    flex-direction: column;
    align-items: center;
    padding-top: 18px;
  }
  .pillar svg { width: 96px; height: 82px; }
  .pillar-label {
    font-family: "Bebas Neue", "Arial Narrow", sans-serif;
    font-size: 27px;
    line-height: 1;
    margin-top: 6px;
  }
  .statement {
    position: absolute;
    left: 92px;
    width: 670px;
  }
  .kicker {
    font-family: "Bebas Neue", "Arial Narrow", sans-serif;
    font-size: 27px;
    line-height: 27px;
  }
  .heading {
    font-family: "Bebas Neue", "Arial Narrow", sans-serif;
    font-weight: 400;
    font-size: 50px;
    line-height: 40px;
    color: var(--orange);
  }
  .body {
    font-weight: 600;
    font-size: 15.6px;
    line-height: 18px;
    text-transform: uppercase;
    margin-top: 5px;
    hyphens: auto;
  }
  .body + .body { margin-top: 18px; }
  .s-id { top: 376px; }
  .s-id .body { margin-top: 1px; }
  .s-mission { top: 473px; }
  .s-werte { top: 599px; }
  .s-vision { top: 726px; }
</style>
</head>
<body>
<div class="poster">
  <div class="skyline" role="img" aria-label="Dezente Stadtsilhouette aus kleinen Quadraten im Hintergrund"></div>

  <header class="brand">
    <span class="brand-name">tlv bau</span>
    <span class="brand-tagline">Digitale Wege im Bau</span>
  </header>

  <section class="pillars">
    <div class="pillar">
      <svg viewBox="0 0 96 82" fill="none" stroke="#fff" stroke-width="2.4" stroke-linecap="round">
        <path d="M28 62 V30 a20 20 0 0 1 40 0 V56"/>
        <path d="M36 66 V31 a12 12 0 0 1 24 0 V62"/>
        <path d="M44 70 V32 a4 4 0 0 1 8 0 V66"/>
        <path d="M22 52 V28 a26 26 0 0 1 52 0 V48"/>
      </svg>
      <span class="pillar-label">Identität</span>
    </div>
    <div class="pillar">
      <svg viewBox="0 0 96 82" fill="none" stroke="#fff" stroke-width="2.4" stroke-linecap="round">
        <path d="M36 56 C22 48 18 36 20 26 A26 26 0 0 1 70 20"/>
        <path d="M60 56 C66 52 70 46 72 38"/>
        <circle cx="46" cy="30" r="16"/>
        <circle cx="46" cy="30" r="7"/>
        <path d="M46 30 L80 22 M74 18 L80 22 L76 28"/>
        <path d="M36 62 H60 M36 68 H60 M40 74 H56"/>
      </svg>
      <span class="pillar-label">Mission</span>
    </div>
    <div class="pillar">
      <svg viewBox="0 0 96 82" fill="none" stroke="#fff" stroke-width="2.4" stroke-linejoin="round">
        <path d="M28 12 H68 L88 32 L48 74 L8 32 Z"/>
        <path d="M8 32 H88 M28 12 L38 32 L48 12 L58 32 L68 12 M38 32 L48 74 M58 32 L48 74"/>
      </svg>
      <span class="pillar-label">Werte</span>
    </div>
    <div class="pillar">
      <svg viewBox="0 0 96 82" fill="none" stroke="#fff" stroke-width="2.4" stroke-linecap="round">
        <path d="M6 42 C22 20 74 20 90 42 C74 64 22 64 6 42 Z"/>
        <circle cx="48" cy="42" r="17"/>
        <circle cx="48" cy="42" r="9"/>
        <path d="M18 24 C34 8 66 8 84 26"/>
      </svg>
      <span class="pillar-label">Vision</span>
    </div>
  </section>

  <section class="statement s-id">
    <p class="kicker">Mein</p>
    <h2 class="heading">ID-Statement</h2>
    <p class="body">Ich bin der klare Laser Richtung Freiheit!</p>
  </section>

  <section class="statement s-mission">
    <p class="kicker">Meine</p>
    <h2 class="heading">Mission</h2>
    <p class="body">Ich fördere Menschen, die mir vertrauen, um gemeinsam Wunder gesche&shy;hen zu lassen, die uns im Herzen verbinden.</p>
  </section>

  <section class="statement s-werte">
    <p class="kicker">Meine</p>
    <h2 class="heading">Werte</h2>
    <p class="body">Authentizität, Integrität, Gestalten, Begeisterung, Verantwortung, Men&shy;schlichkeit, Empathie, Klarheit, Transparenz, Weisheit, Weitblick, Erfolg</p>
  </section>

  <section class="statement s-vision">
    <p class="kicker">Meine</p>
    <h2 class="heading">Vision</h2>
    <p class="body">Ich vertraue den Mitarbeitenden und bin offen. Offenheit meint dabei sowohl den offenen Umgang mit Informationen, als auch die Offenheit für Neues und die Freude am Experimentieren.</p>
    <p class="body">Ich begegne allen Mitarbeitenden auf Augenhöhe. Visionen und Ziele werden gemeinsam entwickelt. Es zählen die besten Argumente und Ideen, keine anderen Faktoren wie Position, Alter, Geschlecht oder Herkunft.</p>
    <p class="body">Ich begleite und fördere meine Mitarbeitenden. Dazu schaffe ich die not&shy;wendigen Räume und Möglichkeiten: Ich gestalte damit den Rahmen und die Struktur für höchste «Performance», und lasse den Mitarbeitenden maximalen Gestaltungsspielraum.</p>
    <p class="body">Ich fördere und fordere in meiner Organisation Schnelligkeit, Agilität und Flexibilität.</p>
    <p class="body">Ich sorge dafür, dass uns in allen Aktivitäten stets das weltweit best&shy;mögliche Wissen zur Verfügung steht und baue dafür auf aktiv gelebte Partnerschaften.</p>
  </section>
</div>
</body>
</html>
```